Sports Nutrition Supplement Label design

We need a sports supplement label design for an existing business. (I have provided our business logo in the file uploads) These labels will remain consistent across the product line with the name of the product being the only changing field. The current product names (example: "vegan") on the labels provided are just for reference, the ingredients portions etc are final, but the actual name will be changed to something less generic for each product. I will just need to be able to change the name and have it match with label concept. We would like the look to be professional, clean, and exemplify quality. Please reference our business website tidelinevigor.com to get a feel for design and brand association.
I have also included the NKB supplement label guidelines so we are certain to maintain compliance.
Thank you and I'm looking forward to working with you and seeing your creative designs!
Darin

Target Market(s)

Athletes, Sports professionals, Colleges, Professional Sports Teams

Industry/Entity Type

Sports Science/ Sports Training/Athletics

Requirements
Nice to have
• I would like the design to possibly reflect these key terms: Sport Science, Chemistry, Clean, Professional, Quality (We also like water/ocean/waves concepts but is not a "requirement" it would have to really work well in the design somehow to appeal to wide range of athletes)

```html
<!DOCTYPE html>
<html lang="en">
<head>
<meta charset="utf-8">
<title>Tideline Vigor – Vegan Chocolate Milkshake Label</title>
<link rel="stylesheet" href="https://fonts.googleapis.com/css2?family=Raleway:wght@400&family=Montserrat:wght@600;700&family=Russo+One&display=swap">
<style>
  :root {
    --page-bg: #eceeef;
    --label-black: #0b0b0c;
    --brand-white: #ffffff;
    --silver-light: #e4e4e4;
    --silver-mid: #a9a9a9;
    --silver-dark: #6d6d6d;
    --gold-light: #fde39a;
    --gold-mid: #e0a83a;
    --gold-dark: #8a5a12;
    --orange: #f07f2e;
    --orange-dark: #d4611a;
    --blue-light: #1f96c6;
    --blue-dark: #0c5c86;
    --circuit-grey: #5a5a5a;
  }
  html, body {
    margin: 0;
    padding: 0;
    width: 1200px;
    height: 1200px;
    overflow: hidden;
    background: var(--page-bg);
  }
  .canvas {
    position: relative;
    width: 1200px;
    height: 1200px;
    display: flex;
    align-items: center;
    justify-content: center;
  }
  .label {
    width: 1120px;
    height: 740px;
    display: block;
    box-shadow: 0 20px 50px rgba(0,0,0,0.25);
  }
  .brand-name {
    font-family: "Raleway", sans-serif;
    font-weight: 400;
    font-size: 74px;
    letter-spacing: 12px;
    fill: var(--brand-white);
  }
  .product-name {
    font-family: "Russo One", sans-serif;
    font-size: 150px;
    letter-spacing: 2px;
    stroke: var(--gold-dark);
    stroke-width: 2;
  }
  .flavor-name {
    font-family: "Montserrat", sans-serif;
    font-weight: 700;
    font-size: 32px;
    fill: var(--brand-white);
  }
  .flavor-type {
    font-family: "Montserrat", sans-serif;
    font-weight: 700;
    font-size: 50px;
    letter-spacing: 2px;
    fill: var(--brand-white);
  }
  .net-weight {
    font-family: "Montserrat", sans-serif;
    font-weight: 600;
    font-size: 22px;
    letter-spacing: 1px;
    fill: var(--brand-white);
  }
  .circuit-line {
    fill: none;
    stroke: var(--circuit-grey);
    stroke-width: 3;
  }
  .circuit-dot {
    fill: var(--silver-light);
  }
</style>
</head>
<body>
<main class="canvas">
  <svg class="label" viewBox="0 0 1120 740" xmlns="http://www.w3.org/2000/svg" aria-label="Tideline Vigor Vegan Chocolate Milkshake supplement label">
    <defs>
      <linearGradient id="silverBand" x1="0" y1="0" x2="1" y2="1">
        <stop offset="0" stop-color="var(--silver-light)"/>
        <stop offset="0.55" stop-color="var(--silver-mid)"/>
        <stop offset="1" stop-color="var(--silver-dark)"/>
      </linearGradient>
      <linearGradient id="goldText" x1="0" y1="0" x2="0" y2="1">
        <stop offset="0" stop-color="var(--gold-light)"/>
        <stop offset="0.5" stop-color="var(--gold-mid)"/>
        <stop offset="1" stop-color="var(--gold-dark)"/>
      </linearGradient>
      <linearGradient id="blueBand" x1="0" y1="0" x2="1" y2="1">
        <stop offset="0" stop-color="var(--blue-light)"/>
        <stop offset="1" stop-color="var(--blue-dark)"/>
      </linearGradient>
      <linearGradient id="orangeBanner" x1="0" y1="0" x2="0" y2="1">
        <stop offset="0" stop-color="var(--orange)"/>
        <stop offset="1" stop-color="var(--orange-dark)"/>
      </linearGradient>
    </defs>

    <rect class="label-base" x="0" y="0" width="1120" height="740" fill="var(--label-black)"/>

    <polygon class="flavor-band" points="0,560 250,560 320,478 1120,410 1120,680 0,680" fill="url(#blueBand)"/>

    <polygon class="product-band" points="170,440 210,330 860,330 1120,205 1120,300 920,400 880,440" fill="url(#silverBand)"/>

    <g class="circuits">
      <polyline class="circuit-line" points="40,395 150,395"/>
      <circle class="circuit-dot" cx="150" cy="395" r="6"/>
      <polyline class="circuit-line" points="1000,255 1000,460 940,520"/>
      <circle class="circuit-dot" cx="940" cy="520" r="6"/>
      <polyline class="circuit-line" points="90,520 220,520"/>
      <polyline class="circuit-line" points="1080,450 1080,560"/>
    </g>

    <text class="brand-name" x="560" y="225" text-anchor="middle">TIDELINE VIGOR</text>

    <g transform="translate(530 435) skewX(-8)">
      <text class="product-name" x="0" y="0" text-anchor="middle" fill="url(#goldText)">VEGAN</text>
    </g>

    <g transform="rotate(-6 515 495)">
      <polygon class="flavor-banner" points="275,462 775,462 757,528 257,528" fill="url(#orangeBanner)"/>
      <text class="flavor-name" x="516" y="507" text-anchor="middle" textLength="430" lengthAdjust="spacingAndGlyphs">CHOCOLATE MILKSHAKE</text>
    </g>

    <text class="flavor-type" x="560" y="610" text-anchor="middle">NATURAL FLAVOR</text>
    <text class="net-weight" x="560" y="648" text-anchor="middle">DIETARY SUPPLEMENT | NET WT. 907 G (2 LB)</text>
  </svg>
</main>
</body>
</html>
```